Business Card design for new private practice opening

I need a business card design for my new private practice with my new logo uploaded as a file
On the front the logo
On the back: maybe a small logo somewhere?
Priv. Doz. DDr. Corinna Vestaluk
Fachärztin für Allgemein- & Viszeralchirurgie
Address: xxx
Tel: xxx
Mobil:xxx
Webseite:xxx
Email:xxx

Contact Information for Business Card

See project description above for details

Requirements
Nice to have
• I would like the colors of the logo incorporated into the business card

```html
<!DOCTYPE html>
<html lang="de">
<head>
<meta charset="utf-8">
<title>Visitenkarte – Priv. Doz. DDr. Corinna Vestaluk</title>
<link rel="stylesheet" href="https://fonts.googleapis.com/css2?family=Cormorant+Garamond:wght@500&family=Fira+Sans:wght@300;400&display=swap">
<style>
  :root {
    --teal: #66b3b4;
    --teal-line: #7cc0c1;
    --grey-text: #707070;
    --grey-icon: #7a7a7a;
    --paper: #ffffff;
    --backdrop: #efefef;
  }
  html, body {
    margin: 0;
    padding: 0;
    width: 1200px;
    height: 800px;
    overflow: hidden;
    background: var(--backdrop);
  }
  .canvas {
    position: relative;
    width: 1200px;
    height: 800px;
  }
  .card {
    position: absolute;
    box-sizing: border-box;
    background: var(--paper);
    border: 3px solid var(--teal-line);
  }
  /* Front side */
  .card-front {
    left: 192px;
    top: 37px;
    width: 606px;
    height: 336px;
    display: flex;
    align-items: center;
    justify-content: center;
  }
  .brand {
    display: flex;
    align-items: center;
    gap: 14px;
  }
  .brand-dot {
    width: 34px;
    height: 34px;
    border-radius: 50%;
    background: var(--teal);
  }
  .brand-name {
    font-family: "Cormorant Garamond", serif;
    font-weight: 500;
    font-size: 34px;
    color: var(--teal);
  }
  /* Back side */
  .card-back {
    left: 403px;
    top: 412px;
    width: 616px;
    height: 336px;
    display: flex;
    border-left: none;
  }
  .side-band {
    width: 152px;
    flex: none;
    background: var(--teal);
    display: flex;
    flex-direction: column;
    align-items: center;
    padding-top: 42px;
    box-sizing: border-box;
    gap: 10px;
  }
  .band-dot {
    width: 44px;
    height: 44px;
    border-radius: 50%;
    background: var(--paper);
  }
  .band-name {
    font-family: "Cormorant Garamond", serif;
    font-weight: 500;
    font-size: 20px;
    color: var(--paper);
  }
  .details {
    padding: 44px 0 0 29px;
    width: 417px;
  }
  .doctor-name {
    margin: 0;
    font-family: "Cormorant Garamond", serif;
    font-weight: 500;
    font-size: 29px;
    line-height: 1;
    color: var(--teal);
    white-space: nowrap;
  }
  .specialty {
    margin: 12px 0 0;
    font-family: "Fira Sans", sans-serif;
    font-weight: 300;
    font-size: 16.5px;
    color: var(--grey-text);
    white-space: nowrap;
  }
  .divider {
    margin: 18px 0 0;
    border: none;
    border-top: 1px solid var(--teal-line);
  }
  .contact-list {
    list-style: none;
    margin: 24px 0 0;
    padding: 0;
  }
  .contact-item {
    display: flex;
    align-items: center;
    height: 34px;
    font-family: "Fira Sans", sans-serif;
    font-weight: 300;
    font-size: 17.5px;
    color: var(--grey-text);
  }
  .contact-icon {
    width: 18px;
    height: 18px;
    margin-right: 10px;
    fill: var(--grey-icon);
    flex: none;
  }
</style>
</head>
<body>
<main class="canvas">
  <section class="card card-front" aria-label="Vorderseite">
    <div class="brand">
      <span class="brand-dot"></span>
      <span class="brand-name">Corinna Vestaluk</span>
    </div>
  </section>

  <section class="card card-back" aria-label="Rückseite">
    <div class="side-band">
      <span class="band-dot"></span>
      <span class="band-name">Vestaluk</span>
    </div>
    <div class="details">
      <h1 class="doctor-name">Priv. Doz. DDr. Corinna Vestaluk</h1>
      <p class="specialty">Fachärztin für Allgemein- &amp; Viszeralchirurgie</p>
      <hr class="divider">
      <ul class="contact-list">
        <li class="contact-item">
          <svg class="contact-icon" viewBox="0 0 24 24"><path d="M12 2a7 7 0 0 0-7 7c0 5 7 13 7 13s7-8 7-13a7 7 0 0 0-7-7zm0 9.5A2.5 2.5 0 1 1 12 6.5a2.5 2.5 0 0 1 0 5z"/></svg>
          Adress: xxx
        </li>
        <li class="contact-item">
          <svg class="contact-icon" viewBox="0 0 24 24"><path d="M6.6 10.8a15 15 0 0 0 6.6 6.6l2.2-2.2a1 1 0 0 1 1-.25 11 11 0 0 0 3.6.6 1 1 0 0 1 1 1V20a1 1 0 0 1-1 1A17 17 0 0 1 3 4a1 1 0 0 1 1-1h3.5a1 1 0 0 1 1 1 11 11 0 0 0 .6 3.6 1 1 0 0 1-.25 1z"/></svg>
          Tel: xxx
        </li>
        <li class="contact-item">
          <svg class="contact-icon" viewBox="0 0 24 24"><path d="M7 1h10a2 2 0 0 1 2 2v18a2 2 0 0 1-2 2H7a2 2 0 0 1-2-2V3a2 2 0 0 1 2-2zm0 3v14h10V4zm5 15.2a1 1 0 1 0 0 2 1 1 0 0 0 0-2z"/></svg>
          Mobil: xxx
        </li>
        <li class="contact-item">
          <svg class="contact-icon" viewBox="0 0 24 24" fill="none" stroke="#7a7a7a" stroke-width="1.8"><circle cx="12" cy="12" r="9.5"/><ellipse cx="12" cy="12" rx="4" ry="9.5"/><path d="M2.5 12h19M4 7h16M4 17h16"/></svg>
          Webseite: xxx
        </li>
        <li class="contact-item">
          <svg class="contact-icon" viewBox="0 0 24 24"><path d="M2 5h20v14H2zm2 2v.5l8 5 8-5V7z"/></svg>
          Email: xxx
        </li>
      </ul>
    </div>
  </section>
</main>
</body>
</html>
```